Seafood Retailer requires varies packaging labels

We are an established business (Restaurant, Seafood Retailer and Crayfish Wholesaler). We have just got a new logo which covers all three aspects of our business (via Artbazaar!). We have always sold cellar door but have been asked by several food outlets to stock our product but as you will see from our pictures - it needs some serious work to take us to the next level. We have a well known finer dining restaurant which we use all these products in and is how several products came about on our Seafood shop shelves. The products are of high quality (just not the labelling). We now want to package our Seafood Retail Shop with professional packaging and labelling and reflect the "quality and freshness" of our products. We have several items we want to label as per below.

If we were to use a slogan it would be "Its about the Freshness and Quality" but not necessary.

We are after a label for our Pickled Seafood 350g tub (Various) - conical container 9cm high x 9cm (top), 7cm (bottom) ONLY but will also try and utilise it to be consistent with the other products following.

Salt and Pepper MIx 250g - conical container (as above)
Smoked Fish (Various weight & fish) - 21cm x 25cm vacuum sealed bags.
Kilpatrick Sauce 250ml - square bottle 22cm high x 4.5cm wide
Minty Lime Vinaigrette 250ml - 23cm round bottle - 4.7cm dia.
Smoked Spicy Salt 75g- 13cm wide x 16cm high vacuum bag
Dukkah 75g - 13cm wide x 16cm high vacuum bag
Lobster Oil 150ml - 18cm x 4.5cm dia round bottle

We will need a working file so we can change the names for the pickled seafood as needed.

I have attached photos of our current products for true understanding of what we currently have had to get by and where we wish to go.

We have a label printer that can print black type overs eg the name of each product so we can have generic coloured labels which we can print over with the change of each product.

We want something that will become a recognisable label.
Updates

Attn Designers.
We are only after one design but which we will use as a guide for all the options supplied as a starting point. The Pickled containers will probably be where we start but happy with any submissions. I probably wasnt very clear but wanted to show all the things we will be using the labelling for so that we can get some continuity We are just after some direction on a good look.  Thanks Melda

Reason: Had some technical problems and wish to extend the time to allow more time conversing with designers.

Target Market(s)

Our target market varies but generally 30 - 65 years in the more affluent background. We are located "literally in the middle of a paddock in the middle of nowhere" (near several holiday villages) and it is the reputation of our premium, fresh products that have people returning and amazed on their first experience.

Industry/Entity Type

Restaurant

Requirements
Must have
• All:

Our logo and the colours are:
Orange
C 13%
M 79%
Y 100%
K 3%

Blue
C 100%
M 96%
Y 14%
K 3%

weight

nutrition panel, barcode (but we can also do that as a separate label on the back ourselves if needed)

"Produced & packaged by:
Copper Reef Foods Pty Ltd, 40271 Danvers Highway, Millicoon SA 5630
Ph: 08 87316042"

Made in Australia from local and imported ingredients. Keep refrigerated. Store at 1oC - 4oC. Use in 7 days after opening.

Nice to have
• Pickled seafood - "Gourmet Pickled" and "Ready to Eat"
Should not have
• Use only the "Copper Reef Foods" logo (not the "Copper Reef Restaurant & Seafood Sales or Restaurant Only logos)

```html
<!DOCTYPE html>
<html lang="en">
<head>
<meta charset="utf-8">
<title>Copper Reef Foods – Pickled Seafood Labels</title>
<link rel="stylesheet" href="https://fonts.googleapis.com/css2?family=Josefin+Sans:wght@600;700&family=Sansita:wght@800&display=swap">
<style>
  :root {
    --backdrop: #808184;
    --brand-blue: #2e3189;
    --brand-orange: #c9531f;
    --ribbon-shade: #a9431a;
    --variant-ink: #2a2a3a;
    --sky-top: #ffffff;
    --sky-mid: #e4effa;
    --sky-bottom: #6aa6de;
    --wave-light: #4a93dc;
    --wave-dark: #2358ad;
    --white: #ffffff;
  }
  html, body {
    margin: 0;
    padding: 0;
    width: 1019px;
    height: 1200px;
    overflow: hidden;
    background: var(--backdrop);
  }
  .label-sheet { display: block; width: 1019px; height: 1200px; }
  .brand-name {
    font-family: "Josefin Sans", sans-serif;
    font-weight: 700;
    fill: var(--brand-orange);
  }
  .product-title {
    font-family: "Sansita", sans-serif;
    font-weight: 800;
    fill: var(--white);
    stroke: var(--brand-blue);
    stroke-width: 6px;
    stroke-linejoin: round;
    paint-order: stroke;
  }
  .variant-name {
    font-family: "Josefin Sans", sans-serif;
    font-weight: 700;
    fill: var(--variant-ink);
    letter-spacing: 1px;
  }
  .net-weight {
    font-family: "Sansita", sans-serif;
    font-weight: 800;
    fill: var(--brand-orange);
    stroke: var(--white);
    stroke-width: 4px;
    paint-order: stroke;
  }
  .storage-note, .producer-info {
    font-family: "Josefin Sans", sans-serif;
    font-weight: 700;
    fill: var(--white);
  }
</style>
</head>
<body>
<svg class="label-sheet" viewBox="0 0 1019 1200" xmlns="http://www.w3.org/2000/svg">
  <defs>
    <radialGradient id="sky-glow" cx="0.5" cy="0.1" r="0.85">
      <stop offset="0" stop-color="var(--sky-top)"/>
      <stop offset="0.5" stop-color="var(--sky-mid)"/>
      <stop offset="1" stop-color="var(--sky-bottom)"/>
    </radialGradient>
    <linearGradient id="wave-fill" x1="0" y1="0" x2="0" y2="1">
      <stop offset="0" stop-color="var(--wave-light)" stop-opacity="0"/>
      <stop offset="0.12" stop-color="var(--wave-light)"/>
      <stop offset="0.55" stop-color="#3577c8"/>
      <stop offset="1" stop-color="var(--wave-dark)"/>
    </linearGradient>
    <radialGradient id="wave-sheen" cx="0.5" cy="0.35" r="0.6">
      <stop offset="0" stop-color="#ffffff" stop-opacity="0.18"/>
      <stop offset="1" stop-color="#ffffff" stop-opacity="0"/>
    </radialGradient>
    <clipPath id="lid-clip"><circle cx="509" cy="345" r="294"/></clipPath>
    <path id="front-arch" d="M 95 898 Q 330 768 565 898"/>
  </defs>

  <!-- Lid label -->
  <g class="lid-label">
    <circle cx="509" cy="345" r="294" fill="url(#sky-glow)"/>
    <g clip-path="url(#lid-clip)" role="img" aria-label="Repeating blue ocean wave pattern">
      <rect x="209" y="372" width="600" height="280" fill="url(#wave-fill)"/>
      <rect x="209" y="372" width="600" height="280" fill="url(#wave-sheen)"/>
    </g>
    <circle cx="509" cy="345" r="294" fill="none" stroke="var(--brand-blue)" stroke-width="13"/>
    <text class="brand-name" x="503" y="228" font-size="40" text-anchor="middle">Copper Reef Foods</text>
    <text class="product-title" x="499" y="352" font-size="66" text-anchor="middle"
          textLength="520" lengthAdjust="spacingAndGlyphs">Pickled Seafood</text>
  </g>

  <!-- Front label -->
  <g class="front-label">
    <rect x="29" y="692" width="602" height="468" fill="url(#sky-glow)"/>
    <g role="img" aria-label="Repeating blue ocean wave pattern">
      <rect x="29" y="930" width="602" height="203" fill="url(#wave-fill)"/>
      <rect x="29" y="930" width="602" height="203" fill="url(#wave-sheen)"/>
    </g>
    <text class="brand-name" x="328" y="764" font-size="34" text-anchor="middle">Copper Reef Foods</text>
    <text class="product-title" font-size="62" text-anchor="middle">
      <textPath href="#front-arch" startOffset="50%">Pickle Seafood</textPath>
    </text>
    <path class="product-window" d="M 130 1035 L 130 920 Q 130 878 200 876 Q 328 868 456 876 Q 526 878 526 920 L 526 1035 Z"
          fill="var(--white)" stroke="var(--brand-orange)" stroke-width="7"/>
    <polygon points="88,1020 124,1020 124,1062 108,1068 88,1068 100,1044" fill="var(--ribbon-shade)"/>
    <polygon points="572,1020 536,1020 536,1062 552,1068 572,1068 560,1044" fill="var(--ribbon-shade)"/>
    <rect x="108" y="1032" width="440" height="36" fill="var(--brand-orange)"/>
    <text class="variant-name" x="328" y="1060" font-size="22" text-anchor="middle">CALAMARI</text>
    <text class="net-weight" x="328" y="1111" font-size="24" text-anchor="middle">350g</text>
    <rect x="29" y="1133" width="602" height="27" fill="var(--brand-blue)"/>
    <text class="storage-note" x="330" y="1153" font-size="15" text-anchor="middle">Keep refrigerated. Store at 1oC - 4oC. Use in 7 days after opening</text>
  </g>

  <!-- Back label -->
  <g class="back-label">
    <rect x="662" y="690" width="358" height="470" fill="url(#sky-glow)"/>
    <g role="img" aria-label="Repeating blue ocean wave pattern">
      <rect x="662" y="935" width="358" height="155" fill="url(#wave-fill)"/>
      <rect x="662" y="935" width="358" height="155" fill="url(#wave-sheen)"/>
    </g>
    <rect class="nutrition-panel" x="718" y="717" width="219" height="221" rx="18"
          fill="var(--white)" stroke="var(--brand-blue)" stroke-width="3"/>
    <rect class="barcode-space" x="762" y="1000" width="132" height="60" fill="var(--white)"/>
    <rect x="662" y="1090" width="358" height="70" fill="var(--brand-blue)"/>
    <g class="producer-info" font-size="9.5" text-anchor="middle">
      <text x="828" y="1103">Made in Australia from local and imported ingredients.</text>
      <text x="828" y="1115">Produced &amp; packaged by:</text>
      <text x="828" y="1127">Copper Reef Foods Pty Ltd, 40271 Danvers Highway,</text>
      <text x="828" y="1139">Millicoon SA 5630</text>
      <text x="828" y="1151">Ph: 08 87316042</text>
    </g>
  </g>
</svg>
</body>
</html>
```